Next-Gen B2B Sales Negotiation App - UI Design for iOS

Develop a user-friendly dark-mode interface for a B2B sales negotiation assistant app for a company called Quorvel. The UI will showcase a single screen with features like counterparty search, agenda selection, and email drafting. Design should reflect a functional iOS app with realistic placeholder data to create a genuine experience.

Precise task description in attachment.

Target Market(s)

B2B

Requirements
Must have
• Each UI picture should look like a screen capture of an iphone
Nice to have
• The UI designs need to show the navigation and the app in use

```html
<!DOCTYPE html>
<html lang="en">
<head>
<meta charset="utf-8">
<title>Quorvel – Negotiation Assistant Screens</title>
<link href="https://fonts.googleapis.com/css2?family=Outfit:wght@400;500;600;700&display=swap" rel="stylesheet">
<style>
:root{
  --canvas:#ffffff;
  --bg:#0a0b1f;
  --bar:#000000;
  --card:#10122a;
  --card-2:#14163a;
  --line:#20234a;
  --text:#f2f3ff;
  --muted:#8a8db5;
  --dim:#5c5f8a;
  --accent:#5548f0;
  --accent-soft:#8d86ff;
  --accent-bg:#1c1a4a;
  --amber:#f5a524;
  --green:#22c55e;
  --red:#f0506e;
}
*{box-sizing:border-box;margin:0;padding:0}
html,body{width:1200px;height:2623px;overflow:hidden;background:var(--canvas)}
body{position:relative;font-family:'Outfit',sans-serif;color:var(--text)}
svg.i{width:14px;height:14px;fill:none;stroke:currentColor;stroke-width:1.8;stroke-linecap:round;stroke-linejoin:round;flex:none}
.phone{position:absolute;width:307px;height:546px;background:var(--bg);border-radius:10px;overflow:hidden}
.topbar{height:40px;background:var(--bar);display:flex;align-items:center;padding:0 18px;gap:14px;font-size:14px;font-weight:600}
.topbar .i{color:var(--accent-soft)}
.topbar .end{margin-left:auto}
.avatar{border-radius:50%;flex:none;background:radial-gradient(circle at 50% 40%,#d9c7b0 0 30%,#6a7fa8 70%)}
.av-b{background:radial-gradient(circle at 50% 45%,#9a9a9a 0 25%,#1e1e24 70%)}
.av-c{background:linear-gradient(160deg,#c8d2dc,#3d4b5c)}
.av-d{background:linear-gradient(180deg,#e8eef0 0 35%,#7a8a4a 60%,#4a5a2a)}
.av-e{background:linear-gradient(180deg,#dfe6ee 0 40%,#d8574a 60%,#f1e4d6)}
.pill{font-size:8px;padding:3px 7px;border-radius:10px;border:1px solid var(--accent);color:var(--accent-soft);background:var(--accent-bg)}
.pill.amber{border-color:#7a5410;color:var(--amber);background:#2a200a}
.tabbar{position:absolute;left:0;right:0;bottom:0;height:56px;border-top:1px solid var(--line);background:var(--bg);display:flex;justify-content:space-around;padding-top:8px}
.tab{display:flex;flex-direction:column;align-items:center;gap:4px;font-size:7px;color:var(--muted);width:50px}
.tab svg.i{width:17px;height:17px}
.tab.on{color:var(--accent-soft)}
.search{display:flex;align-items:center;gap:8px;height:32px;border:1px solid var(--line);border-radius:7px;background:var(--card);padding:0 10px;font-size:10px;color:var(--dim)}
.card{background:var(--card);border:1px solid var(--line);border-radius:9px}
.chev{color:var(--dim);margin-left:auto}
.btn{display:flex;align-items:center;justify-content:center;gap:6px;height:34px;border-radius:7px;background:var(--accent);font-size:12px;font-weight:600}
.label{font-size:8px;letter-spacing:.5px;color:var(--muted);text-transform:uppercase}

.deal{padding:10px 11px;height:73px;margin-bottom:9px}
.deal-head{display:flex;align-items:center;gap:9px}
.deal-name{font-size:10px;font-weight:600}
.deal-sub{font-size:8px;color:var(--muted)}
.deal-head .pill{margin-left:auto}
.deal-foot{display:flex;align-items:center;gap:4px;margin-top:12px;font-size:8px;color:var(--dim)}
.deal-foot b{margin-left:auto;color:var(--text);font-weight:500}
.deal-foot svg.i{width:9px;height:9px}

.person{display:flex;align-items:center;gap:12px}
.person .nm{font-size:11px;font-weight:600}
.person .sub{font-size:9px;color:var(--muted);margin-top:2px}

.agenda{padding:14px 12px 12px}
.agenda-head{display:flex;align-items:center;gap:10px;font-size:11px;font-weight:600}
.ico{width:24px;height:24px;border-radius:6px;background:var(--accent-bg);display:flex;align-items:center;justify-content:center;color:var(--accent-soft)}
.ico svg.i{width:13px;height:13px}
.agenda p{font-size:9px;color:var(--dim);line-height:16px;margin:10px 0 6px 43px}
.agenda p.short{font-size:9.5px;line-height:14px;margin:7px 0 0;max-width:230px}
.tone{margin-left:43px;display:inline-block;font-size:7px;letter-spacing:.3px;border:1px solid var(--line);border-radius:3px;padding:3px 5px;color:#c9cbef}

.chips{display:flex;gap:6px;padding:12px 12px 0}
.chip{display:flex;align-items:center;gap:5px;height:24px;padding:0 8px 0 3px;border-radius:12px;background:var(--card-2);border:1px solid var(--line);font-size:8px}
.chip.accent{padding:0 9px;background:var(--accent-bg);border-color:var(--accent);color:var(--accent-soft)}

.draft{position:absolute;left:12px;right:12px;top:90px;height:376px;border-radius:8px;border:1px solid var(--line);background:#0c0d24;overflow:hidden}
.copy{position:absolute;right:11px;bottom:9px;font-size:8px;color:var(--dim)}
.send{position:absolute;left:12px;right:12px;top:489px}
</style>
</head>
<body>
<svg width="0" height="0" style="position:absolute">
  <defs>
    <symbol id="back" viewBox="0 0 24 24"><path d="M15 5l-7 7 7 7"/></symbol>
    <symbol id="right" viewBox="0 0 24 24"><path d="M9 5l7 7-7 7"/></symbol>
    <symbol id="search" viewBox="0 0 24 24"><circle cx="11" cy="11" r="7"/><path d="M20 20l-4-4"/></symbol>
    <symbol id="case" viewBox="0 0 24 24"><rect x="3" y="7" width="18" height="13" rx="2"/><path d="M9 7V4h6v3M9 7v13M15 7v13"/></symbol>
    <symbol id="bolt" viewBox="0 0 24 24"><path d="M13 3L5 14h6l-1 7 8-11h-6z"/></symbol>
    <symbol id="user" viewBox="0 0 24 24"><circle cx="12" cy="8" r="4"/><path d="M4 21c1-5 15-5 16 0"/></symbol>
    <symbol id="cal" viewBox="0 0 24 24"><rect x="4" y="5" width="16" height="16" rx="2"/><path d="M4 10h16M8 3v4M16 3v4"/></symbol>
    <symbol id="plus" viewBox="0 0 24 24"><path d="M12 5v14M5 12h14"/></symbol>
    <symbol id="refresh" viewBox="0 0 24 24"><path d="M20 11a8 8 0 0 0-14-5l-2 2M4 4v4h4M4 13a8 8 0 0 0 14 5l2-2M20 20v-4h-4"/></symbol>
    <symbol id="hand" viewBox="0 0 24 24"><path d="M4 8l4-3 4 2 4-2 4 3v5l-8 6-8-6z"/><path d="M8 11l4 3 4-3"/></symbol>
    <symbol id="scale" viewBox="0 0 24 24"><path d="M12 4v16M7 20h10M5 7h14M5 7l-3 6h6zM19 7l-3 6h6z"/></symbol>
    <symbol id="check-c" viewBox="0 0 24 24"><circle cx="12" cy="12" r="9"/><path d="M8 12l3 3 5-6"/></symbol>
    <symbol id="tick" viewBox="0 0 24 24"><path d="M5 12l5 5 9-10"/></symbol>
    <symbol id="out" viewBox="0 0 24 24"><path d="M8 16L16 8M9 8h7v7"/></symbol>
    <symbol id="spark" viewBox="0 0 24 24"><path d="M12 3l2 6 6 2-6 2-2 6-2-6-6-2 6-2zM19 3v4M17 5h4M5 17v4M3 19h4"/></symbol>
    <symbol id="mail" viewBox="0 0 24 24"><rect x="3" y="5" width="18" height="14" rx="2"/><path d="M3 7l9 6 9-6"/></symbol>
    <symbol id="phone" viewBox="0 0 24 24"><path d="M5 4h4l2 5-3 2a11 11 0 0 0 5 5l2-3 5 2v4a2 2 0 0 1-2 2A17 17 0 0 1 3 6a2 2 0 0 1 2-2z"/></symbol>
    <symbol id="pin" viewBox="0 0 24 24"><path d="M12 21s7-6 7-12a7 7 0 0 0-14 0c0 6 7 12 7 12z"/><circle cx="12" cy="9" r="2.5"/></symbol>
    <symbol id="dots" viewBox="0 0 24 24"><circle cx="5" cy="12" r="1"/><circle cx="12" cy="12" r="1"/><circle cx="19" cy="12" r="1"/></symbol>
    <symbol id="clock" viewBox="0 0 24 24"><circle cx="12" cy="12" r="9"/><path d="M12 7v5l3 2"/></symbol>
    <symbol id="bell" viewBox="0 0 24 24"><path d="M6 16V11a6 6 0 0 1 12 0v5l2 2H4zM10 21h4"/></symbol>
    <symbol id="gear" viewBox="0 0 24 24"><circle cx="12" cy="12" r="3"/><path d="M12 2v3M12 19v3M2 12h3M19 12h3M5 5l2 2M17 17l2 2M5 19l2-2M17 7l2-2"/></symbol>
    <symbol id="exit" viewBox="0 0 24 24"><path d="M10 4H5v16h5M14 8l4 4-4 4M18 12H9"/></symbol>
  </defs>
</svg>

<!-- 1 Dashboard -->
<section class="phone" style="left:39px;top:45px;background:linear-gradient(180deg,#000 0,var(--bg) 260px)">
  <div style="padding:36px 18px 0">
    <div style="display:flex;align-items:center">
      <div>
        <div style="font-size:9px;color:#b8badb">Welcome back</div>
        <div style="font-size:20px;font-weight:600;margin-top:3px">Dashboard</div>
      </div>
      <div class="user-badge" style="margin-left:auto;width:28px;height:28px;border-radius:50%;background:var(--accent);display:flex;align-items:center;justify-content:center;font-size:10px;font-weight:600">JD</div>
    </div>
    <div style="margin-top:19px;height:120px;border-radius:10px;background:linear-gradient(120deg,#4f3ff0,#8a3bec);padding:16px 14px">
      <div style="font-size:13px;font-weight:600">Start Negotiation</div>
      <div style="font-size:9px;line-height:14px;margin-top:5px;width:180px;color:#e6e2ff">Launch a new tailored strategy with AI assistance.</div>
      <div style="margin-top:11px;width:85px;height:26px;border-radius:5px;background:#fff;color:var(--accent);font-size:9px;display:flex;align-items:center;justify-content:center;gap:4px"><svg class="i" style="width:10px;height:10px"><use href="#plus"/></svg>New Deal</div>
    </div>
    <div style="display:flex;align-items:baseline;margin:28px 0 12px"><span style="font-size:12px;font-weight:600">Active Deals</span><span style="margin-left:auto;font-size:8px;color:var(--accent-soft)">View All</span></div>
    <div class="card deal"><div class="deal-head"><div class="avatar" style="width:28px;height:28px" role="img" aria-label="Portrait of Sarah Chen"></div><div><div class="deal-name">TechFlow Dynamics</div><div class="deal-sub">Sarah Chen</div></div><span class="pill">Negotiation</span></div><div class="deal-foot"><svg class="i"><use href="#cal"/></svg>Sent proposal v2<b>$120,000</b></div></div>
    <div class="card deal"><div class="deal-head"><div class="avatar av-b" style="width:28px;height:28px" role="img" aria-label="Portrait of Marcus Thorne"></div><div><div class="deal-name">Apex Logistics</div><div class="deal-sub">Marcus Thorne</div></div><span class="pill">Discovery</span></div><div class="deal-foot"><svg class="i"><use href="#cal"/></svg>Meeting scheduled<b>$450,000</b></div></div>
    <div class="card deal"><div class="deal-head"><div class="avatar av-d" style="width:28px;height:28px" role="img" aria-label="Portrait of David Kim"></div><div><div class="deal-name">Orbital Systems</div><div class="deal-sub">David Kim</div></div><span class="pill amber">Closing</span></div><div class="deal-foot"><svg class="i"><use href="#cal"/></svg>Legal review<b>$1,200,000</b></div></div>
  </div>
  <nav class="tabbar"><div class="tab on"><svg class="i"><use href="#case"/></svg>Deals</div><div class="tab"><svg class="i"><use href="#search"/></svg>Search</div><div class="tab"><svg class="i"><use href="#bolt"/></svg>Activity</div><div class="tab"><svg class="i"><use href="#user"/></svg>Profile</div></nav>
</section>

<!-- 2 Select Counterparty -->
<section class="phone" style="left:439px;top:49px">
  <div class="topbar"><svg class="i"><use href="#back"/></svg>Select Counterparty</div>
  <div style="padding:12px 12px 0">
    <div class="search"><svg class="i"><use href="#search"/></svg>Search companies or people...</div>
  </div>
  <div style="padding:20px 21px 0;display:flex;flex-direction:column;gap:23px">
    <div class="person"><div class="avatar" style="width:36px;height:36px" role="img" aria-label="Portrait of Sarah Chen"></div><div><div class="nm">Sarah Chen</div><div class="sub">CTO @ TechFlow Dynamics</div></div><svg class="i chev"><use href="#right"/></svg></div>
    <div class="person"><div class="avatar av-b" style="width:36px;height:36px" role="img" aria-label="Portrait of Marcus Thorne"></div><div><div class="nm">Marcus Thorne</div><div class="sub">VP of Operations @ Apex Logistics</div></div><svg class="i chev"><use href="#right"/></svg></div>
    <div class="person"><div class="avatar av-c" style="width:36px;height:36px" role="img" aria-label="Portrait of Elena Rodriguez"></div><div><div class="nm">Elena Rodriguez</div><div class="sub">Procurement Director @ GreenLeaf Energy</div></div><svg class="i chev"><use href="#right"/></svg></div>
    <div class="person"><div class="avatar av-d" style="width:36px;height:36px" role="img" aria-label="Portrait of David Kim"></div><div><div class="nm">David Kim</div><div class="sub">Head of Engineering @ Orbital Systems</div></div><svg class="i chev"><use href="#right"/></svg></div>
    <div class="person"><div class="avatar av-e" style="width:36px;height:36px" role="img" aria-label="Portrait of Jessica Vance"></div><div><div class="nm">Jessica Vance</div><div class="sub">COO @ Novus Retail</div></div><svg class="i chev"><use href="#right"/></svg></div>
  </div>
</section>

<!-- 3 Choose Strategy -->
<section class="phone" style="left:831px;top:46px">
  <div class="topbar"><svg class="i"><use href="#back"/></svg>Choose Strategy</div>
  <div style="padding:9px 18px 0">
    <div class="card person" style="height:52px;padding:0 12px;gap:9px"><div class="avatar" style="width:28px;height:28px" role="img" aria-label="Portrait of Sarah Chen"></div><div><div style="font-size:7px;color:var(--muted)">TARGET</div><div style="font-size:9px;font-weight:600">TechFlow Dynamics</div></div></div>
    <div style="font-size:12px;font-weight:600;margin:27px 2px 14px">Recommended Agendas</div>
    <div class="card agenda" style="height:112px;margin-bottom:12px"><div class="agenda-head"><span class="ico"><svg class="i"><use href="#hand"/></svg></span>Initial Outreach<svg class="i chev" style="width:10px"><use href="#right"/></svg></div><p>Introduce Quorvel capabilities and schedule a demo.</p><span class="tone">TONE: PROFESSIONAL &amp; CURIOUS</span></div>
    <div class="card agenda" style="height:112px;margin-bottom:12px"><div class="agenda-head"><span class="ico"><svg class="i"><use href="#scale"/></svg></span>Price Negotiation<svg class="i chev" style="width:10px"><use href="#right"/></svg></div><p>Address budget concerns while maintaining value proposition.</p><span class="tone">TONE: FIRM BUT COLLABORATIVE</span></div>
    <div class="card agenda" style="height:112px;margin-bottom:12px"><div class="agenda-head"><span class="ico"><svg class="i"><use href="#refresh"/></svg></span>Contract Renewal<svg class="i chev" style="width:10px"><use href="#right"/></svg></div><p>Propose renewal terms with a slight upsell for new features.</p><span class="tone">TONE: APPRECIATIVE &amp; STRATEGIC</span></div>
    <div class="card agenda" style="height:112px"></div>
  </div>
</section>

<!-- 4 Draft Email (loading) -->
<section class="phone" style="left:37px;top:657px">
  <div class="topbar"><svg class="i"><use href="#back"/></svg>Draft Email<svg class="i end" style="color:var(--dim)"><use href="#refresh"/></svg></div>
  <div class="chips"><span class="chip"><span class="avatar" style="width:18px;height:18px" role="img" aria-label="Portrait of Sarah Chen"></span>Sarah Chen</span><span class="chip accent">Initial Outreach</span></div>
  <div class="draft">
    <div style="padding:14px 12px;font-size:11px;color:var(--dim)">Draft will appear here...</div>
    <div style="position:absolute;left:0;right:0;top:160px;text-align:center;color:#3a3d6e;font-size:9px"><svg class="i" style="width:28px;height:28px;stroke:#4b45a8"><use href="#spark"/></svg><div style="margin-top:4px">Consulting Quorvel AI...</div></div>
    <span class="copy">Copy to Clipboard</span>
  </div>
  <div class="btn send" style="background:#2f2a8a;color:#8f8ad0">Send to Email Client<svg class="i" style="width:11px"><use href="#out"/></svg></div>
</section>

<!-- 5 Draft Email (ready) -->
<section class="phone" style="left:439px;top:660px">
  <div class="topbar"><svg class="i"><use href="#back"/></svg>Draft Email<svg class="i end"><use href="#refresh"/></svg></div>
  <div class="chips"><span class="chip"><span class="avatar" style="width:18px;height:18px" role="img" aria-label="Portrait of Sarah Chen"></span>Sarah Chen</span><span class="chip accent">Initial Outreach</span></div>
  <div class="draft" style="font-size:12.5px;line-height:20px;color:#e6e7fb">
    <div style="padding:0 12px;margin-top:-10px">
      <p>I'm reaching out from Quorvel because we specialize in empowering leaders like you to achieve precisely that.</p><br>
      <p>Quorvel's platform delivers proactive intelligence and operational excellence specifically designed for complex SaaS environments. We help teams reduce operational overhead, predict performance bottlenecks, and unlock innovation bandwidth without sacrificing reliability.</p><br>
      <p>I'm curious about how you currently approach proactive infrastructure optimization and resource allocation. Would you be open to a brief 15-20 minute chat next week to explore potential synergies and see if there's a fit for</p>
    </div>
    <span class="copy" style="left:0;right:0;bottom:0;height:30px;padding:13px 11px 0;text-align:right;background:#0c0d24;line-height:12px">Copy to Clipboard</span>
  </div>
  <div class="btn send">Send to Email Client<svg class="i" style="width:11px"><use href="#out"/></svg></div>
</section>

<!-- 6 Ready to Send -->
<section class="phone" style="left:831px;top:659px">
  <div style="position:absolute;left:123px;top:173px;width:60px;height:60px;border-radius:50%;background:#0e3a2c;border:1px solid #1a5a40;display:flex;align-items:center;justify-content:center;color:var(--green)"><svg class="i" style="width:26px;height:26px"><use href="#tick"/></svg></div>
  <div style="position:absolute;left:0;right:0;top:250px;text-align:center">
    <div style="font-size:17px;font-weight:700">Ready to Send!</div>
    <div style="font-size:11px;line-height:19px;color:var(--muted);margin:7px auto 0;width:240px">Your draft has been exported. Good luck with the negotiation.</div>
  </div>
  <div class="btn" style="position:absolute;left:38px;right:38px;top:337px;background:#1a1c3a;border:1px solid var(--line)">Return Home</div>
</section>

<!-- 7 Contacts -->
<section class="phone" style="left:38px;top:1272px">
  <div style="padding:36px 18px 0">
    <div style="font-size:21px;font-weight:700">Contacts</div>
    <div class="search" style="margin-top:11px"><svg class="i"><use href="#search"/></svg>Search directory...</div>
    <div style="display:flex;flex-direction:column;gap:31px;margin-top:26px;padding-left:3px">
      <div class="person"><div class="avatar" style="width:36px;height:36px" role="img" aria-label="Portrait of Sarah Chen"></div><div><div class="nm">Sarah Chen</div><div class="sub">CTO</div><div class="sub" style="font-size:8px;color:var(--dim);margin-top:0">TechFlow Dynamics</div></div><svg class="i chev"><use href="#right"/></svg></div>
      <div class="person"><div class="avatar av-b" style="width:36px;height:36px" role="img" aria-label="Portrait of Marcus Thorne"></div><div><div class="nm">Marcus Thorne</div><div class="sub">VP of Operations</div><div class="sub" style="font-size:8px;color:var(--dim);margin-top:0">Apex Logistics</div></div><svg class="i chev"><use href="#right"/></svg></div>
      <div class="person"><div class="avatar av-c" style="width:36px;height:36px" role="img" aria-label="Portrait of Elena Rodriguez"></div><div><div class="nm">Elena Rodriguez</div><div class="sub">Procurement Director</div><div class="sub" style="font-size:8px;color:var(--dim);margin-top:0">GreenLeaf Energy</div></div><svg class="i chev"><use href="#right"/></svg></div>
      <div class="person"><div class="avatar av-d" style="width:36px;height:36px" role="img" aria-label="Portrait of David Kim"></div><div><div class="nm">David Kim</div><div class="sub">Head of Engineering</div><div class="sub" style="font-size:8px;color:var(--dim);margin-top:0">Orbital Systems</div></div><svg class="i chev"><use href="#right"/></svg></div>
      <div class="person"><div class="avatar av-e" style="width:36px;height:36px" role="img" aria-label="Portrait of Jessica Vance"></div><div><div class="nm">Jessica Vance</div><div class="sub">COO</div><div class="sub" style="font-size:8px;color:var(--dim);margin-top:0">Novus Retail</div></div><svg class="i chev"><use href="#right"/></svg></div>
    </div>
  </div>
  <nav class="tabbar"><div class="tab"><svg class="i"><use href="#case"/></svg>Deals</div><div class="tab on"><svg class="i"><use href="#search"/></svg>Search</div><div class="tab"><svg class="i"><use href="#cal"/></svg>Activity</div><div class="tab"><svg class="i"><use href="#user"/></svg>Profile</div></nav>
</section>

<!-- 8 Contact detail -->
<section class="phone" style="left:442px;top:1268px">
  <div class="topbar"><svg class="i"><use href="#back"/></svg><svg class="i end" style="color:var(--muted)"><use href="#dots"/></svg></div>
  <div class="avatar" style="position:absolute;left:122px;top:40px;width:62px;height:62px;border:2px solid var(--accent)" role="img" aria-label="Portrait of Sarah Chen"></div>
  <div style="text-align:center;margin-top:77px">
    <div style="font-size:17px;font-weight:700">Sarah Chen</div>
    <div style="font-size:9px;color:var(--muted);margin-top:5px">CTO at <b style="color:var(--text);font-weight:600">TechFlow Dynamics</b></div>
    <div style="display:flex;justify-content:center;gap:10px;margin-top:14px;color:var(--accent-soft)">
      <span style="width:28px;height:28px;border-radius:50%;background:var(--card-2);border:1px solid var(--line);display:flex;align-items:center;justify-content:center"><svg class="i" style="width:12px"><use href="#mail"/></svg></span>
      <span style="width:28px;height:28px;border-radius:50%;background:var(--card-2);border:1px solid var(--line);display:flex;align-items:center;justify-content:center"><svg class="i" style="width:12px"><use href="#phone"/></svg></span>
      <span style="width:28px;height:28px;border-radius:50%;background:var(--card-2);border:1px solid var(--line);display:flex;align-items:center;justify-content:center"><svg class="i" style="width:12px"><use href="#pin"/></svg></span>
    </div>
  </div>
  <div style="position:absolute;left:0;right:0;top:229px;bottom:0;background:#0d0e26;border-top:1px solid var(--line);padding:18px 18px 0">
    <div class="label">Info</div>
    <div style="display:flex;gap:10px;margin-top:8px">
      <div class="card" style="flex:1;height:48px;padding:10px"><div style="font-size:7px;color:var(--dim)">Industry</div><div style="font-size:10px;font-weight:600;margin-top:5px">SaaS Infrastructure</div></div>
      <div class="card" style="flex:1;height:48px;padding:10px"><div style="font-size:7px;color:var(--dim)">Est. Deal Size</div><div style="font-size:10px;font-weight:600;margin-top:5px">$120k</div></div>
    </div>
    <div class="card" style="height:48px;padding:10px;margin-top:11px"><div style="font-size:7px;color:var(--dim)">Last Contact</div><div style="font-size:10px;font-weight:600;margin-top:5px">2 days ago</div></div>
    <div class="label" style="margin-top:20px">Active Deal</div>
    <div class="card deal" style="margin-top:8px"><div class="deal-head"><div class="avatar" style="width:28px;height:28px" role="img" aria-label="Portrait of Sarah Chen"></div><div><div class="deal-name">TechFlow Dynamics</div><div class="deal-sub">Sarah Chen</div></div><span class="pill">Negotiation</span></div><div class="deal-foot"><svg class="i"><use href="#cal"/></svg>Sent proposal v2<b>$120,000</b></div></div>
  </div>
  <div class="btn" style="position:absolute;left:12px;right:12px;top:500px">Start Negotiation</div>
</section>

<!-- 9 Choose Strategy (full list) -->
<section class="phone" style="left:833px;top:1266px">
  <div class="topbar"><svg class="i"><use href="#back"/></svg><div><div style="font-size:14px;line-height:15px">Choose Strategy</div><div style="font-size:8px;color:var(--muted);font-weight:400">For TechFlow Dynamics</div></div></div>
  <div style="padding:17px 18px 0;display:flex;flex-direction:column;gap:12px">
    <div class="card agenda" style="height:67px"><div class="agenda-head"><span class="ico"><svg class="i"><use href="#hand"/></svg></span>Initial Outreach</div><p class="short" style="max-width:none">Introduce Quorvel capabilities and schedule a demo.</p></div>
    <div class="card agenda" style="height:81px"><div class="agenda-head"><span class="ico"><svg class="i"><use href="#scale"/></svg></span>Price Negotiation</div><p class="short">Address budget concerns while maintaining value proposition.</p></div>
    <div class="card agenda" style="height:81px"><div class="agenda-head"><span class="ico"><svg class="i"><use href="#refresh"/></svg></span>Contract Renewal</div><p class="short">Propose renewal terms with a slight upsell for new features.</p></div>
    <div class="card agenda" style="height:67px"><div class="agenda-head"><span class="ico"><svg class="i"><use href="#check-c"/></svg></span>Closing the Deal</div><p class="short" style="max-width:none">Finalize terms and send the contract for signature.</p></div>
    <div class="card agenda" style="height:81px"><div class="agenda-head"><span class="ico"><svg class="i"><use href="#cal"/></svg></span>Quarterly Check-in</div><p class="short">Review performance and discuss future roadmap alignment.</p></div>
  </div>
</section>

<!-- 10 Activity -->
<section class="phone" style="left:37px;top:1889px">
  <div style="padding:36px 18px 0">
    <div style="display:flex;align-items:center"><span style="font-size:21px;font-weight:700">Activity</span><span style="margin-left:auto;width:22px;height:22px;border-radius:50%;background:var(--card-2);border:1px solid var(--line);display:flex;align-items:center;justify-content:center;color:var(--accent-soft)"><svg class="i" style="width:11px"><use href="#plus"/></svg></span></div>
    <div style="display:flex;gap:8px;margin-top:16px;font-size:9px;white-space:nowrap">
      <span style="background:var(--accent);border-radius:12px;padding:6px 11px">Today</span>
      <span style="background:var(--card-2);border:1px solid var(--line);border-radius:12px;padding:6px 11px;color:#c9cbef">Tomorrow</span>
      <span style="background:var(--card-2);border:1px solid var(--line);border-radius:12px;padding:6px 11px;color:#c9cbef">Wed</span>
      <span style="background:var(--card-2);border:1px solid var(--line);border-radius:12px;padding:6px 11px;color:#c9cbef">Thu</span>
      <span style="background:var(--card-2);border:1px solid var(--line);border-radius:12px;padding:6px 11px;color:#c9cbef">Fri</span>
    </div>
  </div>
  <div style="position:absolute;left:67px;top:150px;width:1px;height:330px;background:var(--line)"></div>
  <div style="position:absolute;left:26px;top:148px;font-size:8px;color:var(--dim);text-align:center;line-height:10px">09:00<br>AM</div>
  <div style="position:absolute;left:65px;top:151px;width:5px;height:5px;border-radius:50%;background:var(--accent-soft)"></div>
  <div class="card" style="position:absolute;left:84px;right:18px;top:145px;height:90px;padding:10px 9px">
    <div style="display:flex"><span class="pill" style="font-size:7px;padding:1px 5px;border-radius:3px">MEETING</span><span style="margin-left:auto;font-size:7px;color:var(--dim);display:flex;gap:2px;align-items:center"><svg class="i" style="width:8px"><use href="#clock"/></svg>45m</span></div>
    <div style="font-size:10px;font-weight:600;margin-top:6px">Strategy Review</div><div style="font-size:8px;color:var(--muted);margin-top:2px">Discuss Q4 roadmap alignment</div>
    <div style="border-top:1px solid var(--line);margin-top:8px;padding-top:7px;display:flex;gap:5px;align-items:center;font-size:8px"><span class="avatar" style="width:13px;height:13px" role="img" aria-label="Portrait of Sarah Chen"></span>Sarah Chen</div>
  </div>
  <div style="position:absolute;left:26px;top:262px;font-size:8px;color:var(--dim);text-align:center;line-height:10px">11:30<br>AM</div>
  <div style="position:absolute;left:65px;top:265px;width:5px;height:5px;border-radius:50%;background:var(--green)"></div>
  <div class="card" style="position:absolute;left:84px;right:18px;top:258px;height:90px;padding:10px 9px">
    <div style="display:flex"><span class="pill" style="font-size:7px;padding:1px 5px;border-radius:3px;border-color:#1a5a40;color:var(--green);background:#0e2a22">CALL</span><span style="margin-left:auto;font-size:7px;color:var(--dim);display:flex;gap:2px;align-items:center"><svg class="i" style="width:8px"><use href="#clock"/></svg>15m</span></div>
    <div style="font-size:10px;font-weight:600;margin-top:6px">Intro Call</div><div style="font-size:8px;color:var(--muted);margin-top:2px">Quick sync on requirements</div>
    <div style="border-top:1px solid var(--line);margin-top:8px;padding-top:7px;display:flex;gap:5px;align-items:center;font-size:8px"><span class="avatar av-e" style="width:13px;height:13px" role="img" aria-label="Portrait of Jessica Vance"></span>Jessica Vance</div>
  </div>
  <div style="position:absolute;left:26px;top:376px;font-size:8px;color:var(--dim);text-align:center;line-height:10px">02:00<br>PM</div>
  <div style="position:absolute;left:65px;top:379px;width:5px;height:5px;border-radius:50%;background:var(--amber)"></div>
  <div class="card" style="position:absolute;left:84px;right:18px;top:372px;height:90px;padding:10px 9px">
    <div style="display:flex"><span class="pill amber" style="font-size:7px;padding:1px 5px;border-radius:3px">EMAIL</span><span style="margin-left:auto;font-size:7px;color:var(--dim);display:flex;gap:2px;align-items:center"><svg class="i" style="width:8px"><use href="#clock"/></svg>20m</span></div>
    <div style="font-size:10px;font-weight:600;margin-top:6px">Send Proposal</div><div style="font-size:8px;color:var(--muted);margin-top:2px">Draft and send initial pricing tiers</div>
    <div style="border-top:1px solid var(--line);margin-top:8px;padding-top:7px;display:flex;gap:5px;align-items:center;font-size:8px"><span class="avatar av-b" style="width:13px;height:13px" role="img" aria-label="Portrait of Marcus Thorne"></span>Marcus Thorne</div>
  </div>
  <nav class="tabbar"><div class="tab"><svg class="i"><use href="#case"/></svg>Deals</div><div class="tab"><svg class="i"><use href="#search"/></svg>Search</div><div class="tab on"><svg class="i"><use href="#cal"/></svg>Activity</div><div class="tab"><svg class="i"><use href="#user"/></svg>Profile</div></nav>
</section>

<!-- 11 Deal Details -->
<section class="phone" style="left:439px;top:1879px">
  <div class="topbar"><svg class="i"><use href="#back"/></svg>Deal Details<span class="end" style="font-size:8px;color:var(--dim);font-weight:400">d1</span></div>
  <div style="padding:16px 18px 0">
    <div style="display:flex;align-items:flex-start"><div><div style="font-size:21px;font-weight:700">$120,000</div><div style="font-size:9px;color:var(--muted);margin-top:2px">Potential Value</div></div><span class="pill" style="margin-left:auto;margin-top:4px;font-size:7.5px;letter-spacing:.3px">NEGOTIATION</span></div>
    <div style="display:flex;font-size:8px;color:var(--muted);margin-top:18px"><span>Probability</span><b style="margin-left:auto;color:var(--text);font-weight:500">60%</b></div>
    <div style="height:5px;border-radius:3px;background:var(--card-2);margin-top:6px"><div style="width:60%;height:100%;border-radius:3px;background:var(--accent)"></div></div>
    <div class="card person" style="height:59px;padding:0 12px;margin-top:30px;gap:11px"><div class="avatar" style="width:34px;height:34px" role="img" aria-label="Portrait of Sarah Chen"></div><div><div class="nm">Sarah Chen</div><div class="sub" style="font-size:8px">TechFlow Dynamics</div></div><svg class="i chev" style="width:11px"><use href="#right"/></svg></div>
    <div class="card" style="height:85px;padding:12px;margin-top:12px">
      <div style="font-size:10px;font-weight:600">Recent Activity</div>
      <div style="display:flex;gap:8px;margin-top:9px"><span style="width:5px;height:5px;border-radius:50%;background:var(--accent-soft);margin-top:4px"></span><div><div style="font-size:9px">Sent proposal v2</div><div style="font-size:7px;color:var(--dim);margin-top:2px">Today</div></div></div>
    </div>
  </div>
</section>

<!-- 12 Profile -->
<section class="phone" style="left:831px;top:1889px">
  <div style="padding:36px 18px 0">
    <div style="font-size:21px;font-weight:700">Profile</div>
    <div style="display:flex;align-items:center;gap:11px;margin-top:15px">
      <div style="width:58px;height:58px;border-radius:50%;background:linear-gradient(135deg,#6a4cf5,#a14ef0);display:flex;align-items:center;justify-content:center;font-size:20px;font-weight:700">JD</div>
      <div><div style="font-size:15px;font-weight:600">John Doe</div><div style="font-size:9px;color:var(--muted);margin-top:1px">Senior Sales Director</div><span style="display:inline-block;margin-top:5px;font-size:7px;color:var(--green);background:#0e2a22;border:1px solid #1a5a40;border-radius:8px;padding:2px 6px">Top Performer</span></div>
    </div>
    <div style="display:flex;gap:10px;margin-top:22px">
      <div class="card" style="flex:1;height:58px;padding:12px"><div class="label" style="font-size:7px">Pipeline</div><div style="font-size:14px;font-weight:600;margin-top:4px">$4.2M</div></div>
      <div class="card" style="flex:1;height:58px;padding:12px"><div class="label" style="font-size:7px">Closed Q4</div><div style="font-size:14px;font-weight:600;margin-top:4px">12</div></div>
    </div>
    <div class="label" style="margin:27px 3px 9px">Settings</div>
    <div style="display:flex;flex-direction:column;gap:4px;font-size:9px;font-weight:600">
      <div class="card" style="height:40px;display:flex;align-items:center;gap:10px;padding:0 12px;border-color:transparent"><svg class="i" style="color:var(--muted)"><use href="#bell"/></svg>Notifications<span style="margin-left:auto;font-size:8px;color:var(--dim);font-weight:400">On</span><svg class="i" style="width:9px;color:var(--dim)"><use href="#right"/></svg></div>
      <div class="card" style="height:40px;display:flex;align-items:center;gap:10px;padding:0 12px;border-color:transparent"><svg class="i" style="color:var(--muted)"><use href="#bolt"/></svg>AI Configuration<span style="margin-left:auto;font-size:8px;color:var(--dim);font-weight:400">Standard</span><svg class="i" style="width:9px;color:var(--dim)"><use href="#right"/></svg></div>
      <div class="card" style="height:40px;display:flex;align-items:center;gap:10px;padding:0 12px;border-color:transparent"><svg class="i" style="color:var(--muted)"><use href="#gear"/></svg>General<svg class="i chev" style="width:9px"><use href="#right"/></svg></div>
      <div class="card" style="height:40px;display:flex;align-items:center;gap:10px;padding:0 12px;border-color:transparent;color:var(--red)"><svg class="i"><use href="#exit"/></svg>Sign Out<svg class="i chev" style="width:9px"><use href="#right"/></svg></div>
    </div>
  </div>
  <nav class="tabbar"><div class="tab"><svg class="i"><use href="#case"/></svg>Deals</div><div class="tab"><svg class="i"><use href="#search"/></svg>Search</div><div class="tab"><svg class="i"><use href="#cal"/></svg>Activity</div><div class="tab on"><svg class="i"><use href="#user"/></svg>Profile</div></nav>
</section>
</body>
</html>
```